Flyer Design

I'm looking for a new flyer design to help promote our landscape company, and some of our main service for the up and coming season. We're trying to position ourselves as a leader in our market, so obviously quality is important to us.

Our current promotion is 25% off the first month with signup of annual service.

Phone Number: (555) 213-0948
Website: verdlanex.com
Our tagline: "Your hands are full... Let us help"

The call to action: direct them to our website for a detailed list of services and to receive a free quote.

You're welcome to add your own wording and punctuation. If I like the design I will provide feedback accordingly.

I have attached a jpg of our logo to help with design colors. I will provide the vector file upon completion of this project.

Also, I've attached a few photos that I had on hand of our companies work that may help with the design. Obviously I don't want to use them all, but there are a couple just to help out. I'm not opposed to stock photos either.
Thanks

Target Market(s)

We market to high end customers, generally with home between $500k-$2mil, or household income over $200k. Quality and creativity are most important to us.

Industry/Entity Type

Landscape

Requirements
Must have
• Creativity, easy to read, modern style.

```html
<!DOCTYPE html>
<html lang="en">
<head>
<meta charset="utf-8">
<title>Verdlane Lawn &amp; Landscape – Seasonal Flyer</title>
<link rel="stylesheet" href="https://fonts.googleapis.com/css2?family=Barlow+Condensed:wght@500;600;700&family=Merriweather:ital,wght@1,700&display=swap">
<style>
  :root {
    --orange: #f26a3d;
    --orange-deep: #e0552a;
    --ink: #2a2a2a;
    --ink-soft: #4a4a4a;
    --cream-top: #f6f3ea;
    --cream-bottom: #d8d5c6;
    --white: #ffffff;
  }
  html, body {
    margin: 0;
    padding: 0;
    width: 861px;
    height: 1200px;
    overflow: hidden;
  }
  p, h1 { margin: 0; }
  .flyer {
    position: relative;
    width: 861px;
    height: 1200px;
    background: linear-gradient(180deg, var(--cream-top) 45%, var(--cream-bottom) 100%);
    font-family: "Barlow Condensed", "Arial Narrow", sans-serif;
    color: var(--ink);
    overflow: hidden;
  }
  .hero {
    position: absolute;
    inset: 0 0 auto 0;
    width: 861px;
    height: 640px;
  }
  .tagline {
    position: absolute;
    left: 62px;
    top: 330px;
    font-family: "Merriweather", Georgia, serif;
    font-style: italic;
    font-weight: 700;
    font-size: 58px;
    line-height: 1.18;
    color: var(--white);
    text-shadow: 2px 3px 6px rgba(0, 0, 0, 0.55);
  }
  .brand {
    position: absolute;
    right: 58px;
    top: 580px;
    display: flex;
    align-items: center;
    gap: 14px;
  }
  .brand-dot {
    width: 40px;
    height: 40px;
    border-radius: 50%;
    background: var(--orange);
  }
  .brand-name {
    font-weight: 700;
    font-size: 58px;
    line-height: 1;
    letter-spacing: 1px;
    color: var(--ink);
    text-transform: uppercase;
  }
  .phone {
    position: absolute;
    left: 64px;
    top: 678px;
    display: flex;
    align-items: center;
    gap: 12px;
    font-weight: 600;
    font-size: 50px;
    line-height: 1;
    color: var(--ink);
  }
  .phone-icon {
    width: 48px;
    height: 48px;
  }
  .offer {
    position: absolute;
    left: 58px;
    top: 716px;
    font-weight: 700;
    font-size: 230px;
    line-height: 1;
    letter-spacing: 4px;
    color: var(--orange);
    text-shadow: 0 -2px 0 var(--orange-deep), 1px 3px 3px rgba(0, 0, 0, 0.18);
  }
  .offer-terms {
    position: absolute;
    left: 62px;
    top: 950px;
    font-weight: 600;
    font-size: 45px;
    line-height: 1.1;
    color: var(--ink);
  }
  .cta {
    position: absolute;
    left: 0;
    right: 0;
    top: 1058px;
    text-align: center;
  }
  .cta-line {
    font-weight: 600;
    font-size: 52px;
    line-height: 1.1;
    color: var(--ink);
  }
  .cta-url {
    color: var(--orange);
  }
  .cta-note {
    margin-top: 6px;
    font-weight: 500;
    font-size: 33px;
    line-height: 1.1;
    color: var(--ink-soft);
  }
</style>
</head>
<body>
  <main class="flyer">
    <svg class="hero" viewBox="0 0 861 640">
      <defs>
        <linearGradient id="hero-tones" x1="0" y1="0" x2="0" y2="1">
          <stop offset="0" stop-color="#e4eaee"/>
          <stop offset="0.22" stop-color="#c9cfd2"/>
          <stop offset="0.38" stop-color="#b89a82"/>
          <stop offset="0.55" stop-color="#7a8f55"/>
          <stop offset="0.75" stop-color="#4f8a34"/>
          <stop offset="1" stop-color="#3f7429"/>
        </linearGradient>
      </defs>
      <polygon role="img" aria-label="Photo of a brick home with a freshly striped green lawn, walkway and tree"
               points="0,0 861,0 861,436 0,600" fill="url(#hero-tones)"/>
      <polygon class="accent-band" points="0,598 861,434 861,458 0,622" fill="var(--orange)"/>
    </svg>

    <h1 class="tagline">Your hands are full...<br>Let us help.</h1>

    <div class="brand">
      <span class="brand-dot"></span>
      <span class="brand-name">Verdlane</span>
    </div>

    <p class="phone">
      <svg class="phone-icon" viewBox="0 0 46 46" aria-hidden="true">
        <circle cx="23" cy="23" r="23" fill="var(--ink)"/>
        <path d="M16 12c1.5-1 3-.6 3.6.6l2 4c.5 1 .2 2-.6 2.7l-1.6 1.2c.9 2.4 2.8 4.4 5.2 5.6l1.3-1.6c.7-.8 1.8-1 2.7-.5l3.8 2.2c1.1.7 1.4 2.2.5 3.5-1.6 2.4-4 3.4-6.6 2.4-5.6-2.2-9.6-6.4-11.6-12-.8-2.6.3-5.2 1.3-8.1z" fill="var(--white)"/>
      </svg>
      (555) 213-0948
    </p>

    <p class="offer">25% OFF</p>
    <p class="offer-terms">the first month with signup of annual service.</p>

    <div class="cta">
      <p class="cta-line">Go to <span class="cta-url">www.verdlanex.com</span></p>
      <p class="cta-note">to see list of services and receive a free quote.</p>
    </div>
  </main>
</body>
</html>
```